Web Design Project

We have a website in beta that needs updating and are looking for a freash new look for the Home page including Logo.
Our company is called " Pim Sa Ox " we specialize in classified advertising using video. Our consumers will be businesses selling a product or service. Please visit www.pimsaox.com
Our aim past this point is to engage a developer to write the code based on the best design. Our target market is the U.S and I have included some of the landing pages to give you a better idea of what we are trying to acheive

http://www.pimsaox.com/
http://www.pimsaox.com/cars_home.php
http://www.pimsaox.com/boats.php
http://www.pimsaox.com/electronic.php
http://www.pimsaox.com/realestate.php
http://www.pimsaox.com/roommates.php

Target Market(s)

20-35 yr old people who are connected to the internet via mobile phone and use social media on a daily/weekly basis

Industry/Entity Type

Advertising

Requirements
Must have
• We would like to use lots of images to convey it is a video driven website business
Nice to have
• Logo to incorporate same theme of website ( ie ) you are here to watch videos of thinhs to buy & sell
Should not have
• This is to be a freash new site with large type and bold fonts

```html
<!DOCTYPE html>
<html lang="en">
<head>
<meta charset="utf-8">
<title>Pim Sa Ox — Video Classifieds</title>
<link href="https://fonts.googleapis.com/css2?family=Source+Sans+Pro:wght@400;600;700&display=swap" rel="stylesheet">
<style>
:root{
  --header-bg:#333132;
  --topline:#1e1d1e;
  --footer-bg:#333132;
  --bottom-bg:#232223;
  --accent:#17a3e6;
  --badge-red:#e0262b;
  --white:#ffffff;
  --text-dark:#3a3a3a;
  --text-light:#bdbdbd;
  --text-muted:#8e8e8e;
  --border:#d5d5d5;
}
*{box-sizing:border-box;margin:0;padding:0}
html,body{width:1200px;height:1174px;overflow:hidden}
body{position:relative;background:var(--white);font-family:"Source Sans Pro",Arial,sans-serif;color:var(--text-dark)}
.abs{position:absolute}

/* header */
.site-header{position:absolute;left:0;top:0;width:1200px;height:217px;background:var(--header-bg);border-top:10px solid var(--topline)}
.brand{left:196px;top:55px;display:flex;align-items:center;gap:10px}
.brand-name{font-size:34px;font-weight:700;color:var(--white);letter-spacing:-0.5px}
.brand-mark{width:24px;height:24px;background:var(--badge-red)}
.header-divider{left:390px;top:38px;height:68px;border-left:1px dotted #5a585a}
.award-badge{left:413px;top:65px;width:130px;height:50px}
.account-links{left:748px;top:89px;height:31px;display:flex;background:var(--white);border:1px solid var(--border)}
.account-links span{font-size:13px;line-height:29px;padding:0 11px;color:var(--text-dark)}
.account-links span+span{border-left:1px solid var(--border)}
.sell-button{left:885px;top:89px;width:126px;height:31px;background:var(--accent);color:var(--white);font-size:13px;display:flex;align-items:center;gap:10px;padding-left:18px;border:1px solid #4fbdf0}
.search-bar{left:188px;top:137px;width:823px;height:37px;display:flex;background:var(--white);border:1px solid var(--border)}
.search-field{width:414px;display:flex;align-items:center;gap:12px;padding-left:14px;font-size:14px;color:#555}
.search-select{display:flex;align-items:center;justify-content:space-between;padding:0 12px 0 18px;font-size:14px;color:#555;border-left:1px solid var(--border)}
.search-select.place{width:164px}
.search-select.category{width:166px}
.search-go{flex:1;background:var(--accent);color:var(--white);font-weight:700;font-size:14px;display:flex;align-items:center;justify-content:center}
.sellers-count{left:188px;top:182px;font-size:9px;color:#a3a3a3}

/* gallery */
.tile{position:absolute;height:144px}
.tile-caption{position:absolute;left:0;bottom:0;width:100%;height:42px;background:rgba(90,90,92,.85);display:flex;align-items:center}
.play-box{width:52px;height:42px;background:var(--accent);display:flex;align-items:center;justify-content:center}
.tile-caption span{margin-left:29px;color:var(--white);font-size:15px}

.social-row{left:143px;top:800px;display:flex;gap:18px}
.social-dot{width:30px;height:30px;border-radius:50%;background:var(--accent)}
.social-row .social-dot:nth-child(2){margin-left:0}
.view-all{left:981px;top:815px;font-size:14px;color:var(--text-dark);display:flex;align-items:center;gap:9px}

/* footer */
.site-footer{position:absolute;left:0;top:870px;width:1200px;height:218px;background:var(--footer-bg)}
.footer-col h4{font-size:12px;font-weight:700;color:var(--white);letter-spacing:.3px;margin-bottom:15px}
.footer-col li{list-style:none;font-size:10px;color:var(--text-light);line-height:17.2px}
.footer-divider{left:743px;top:38px;height:124px;border-left:1px solid #4a484a}
.newsletter{left:816px;top:38px;width:250px}
.newsletter h4{font-size:12px;font-weight:700;color:var(--white);margin-bottom:14px}
.newsletter p{font-size:10px;color:var(--text-light);line-height:17px}
.subscribe-form{display:flex;margin-top:8px}
.subscribe-form .email{width:146px;height:22px;background:var(--white);font-size:10px;color:#555;line-height:22px;padding-left:16px}
.subscribe-form .submit{width:70px;height:22px;background:var(--accent);color:var(--white);font-size:10px;line-height:22px;text-align:center}

.bottom-bar{position:absolute;left:0;top:1088px;width:1200px;height:86px;background:var(--bottom-bg)}
.copyright{left:142px;top:26px;font-size:12px;color:var(--text-light)}
.copyright b{font-weight:400;color:var(--white)}
.legal-links{left:394px;top:26px;display:flex;font-size:12px;color:var(--text-light)}
.legal-links span+span::before{content:"⁝";margin:0 8px;color:#777}
</style>
</head>
<body>

<header class="site-header">
  <div class="abs brand"><span class="brand-name">Pim Sa Ox</span><span class="brand-mark"></span></div>
  <div class="abs header-divider"></div>
  <svg class="abs award-badge" viewBox="0 0 130 50" aria-hidden="true">
    <rect x="12" y="5" width="116" height="29" fill="var(--badge-red)"/>
    <path d="M6 26 L4 48 L11 42 L17 48 L18 26Z" fill="#f0a21e"/>
    <circle cx="12" cy="22" r="11" fill="#f3b63a"/>
  </svg>
  <div class="abs account-links"><span>Login</span><span>Register</span></div>
  <div class="abs sell-button">
    <svg width="12" height="12" viewBox="0 0 12 12"><path d="M6 0v12M0 6h12" stroke="#fff" stroke-width="3"/></svg>
    Star free sell
  </div>
  <div class="abs search-bar">
    <div class="search-field">
      <svg width="16" height="16" viewBox="0 0 16 16"><circle cx="6.5" cy="6.5" r="5" fill="none" stroke="#666" stroke-width="1.6"/><path d="M10.2 10.2 15 15" stroke="#666" stroke-width="1.8"/></svg>
      Looking for something?
    </div>
    <div class="search-select place">Search by place
      <svg width="11" height="7" viewBox="0 0 11 7"><path d="M1 1l4.5 4.5L10 1" stroke="var(--accent)" stroke-width="2" fill="none"/></svg></div>
    <div class="search-select category">Search by categories
      <svg width="11" height="7" viewBox="0 0 11 7"><path d="M1 1l4.5 4.5L10 1" stroke="var(--accent)" stroke-width="2" fill="none"/></svg></div>
    <div class="search-go">GO</div>
  </div>
  <div class="abs sellers-count">2.020.239 people sell on our place</div>
</header>

<main>
  <div class="tile" style="left:143px;top:307px;width:298px;background:linear-gradient(120deg,#9a9ea4,#8d1d22 55%,#4d4f55)" role="img" aria-label="Red car on a wet road"></div>
  <div class="tile" style="left:451px;top:307px;width:298px;background:linear-gradient(180deg,#b9d3e8,#e9eef2 50%,#2f6c9c)" role="img" aria-label="White motor yacht at sea"></div>
  <div class="tile" style="left:759px;top:307px;width:144px;background:linear-gradient(135deg,#c8d98a,#f1ede6 50%,#8b5a36)" role="img" aria-label="Sleeping child with a teddy bear"></div>
  <div class="tile" style="left:913px;top:307px;width:144px;background:linear-gradient(160deg,#3b3d40,#1f2022)" role="img" aria-label="Dancer jumping in a dark room"></div>

  <div class="tile" style="left:143px;top:460px;width:298px;background:linear-gradient(180deg,#c98a45,#e8861c 50%,#b8652a)" role="img" aria-label="Orange sofa with a yellow table"></div>
  <div class="tile" style="left:451px;top:460px;width:298px;background:linear-gradient(120deg,#8a7e70,#3a3d45 40%,#2a2d33)" role="img" aria-label="Headlight of a dark car"></div>
  <div class="tile" style="left:759px;top:460px;width:144px;background:radial-gradient(circle at 55% 45%,#7a2a2f,#2a2a2a 70%)" role="img" aria-label="Red motorbike"></div>
  <div class="tile" style="left:913px;top:460px;width:144px;background:linear-gradient(150deg,#d24a2a,#e08a3a 60%,#c6a060)" role="img" aria-label="Tomato bruschetta"></div>

  <div class="tile" style="left:143px;top:614px;width:144px;background:linear-gradient(150deg,#c9cccb,#a8312f 60%,#5b5b5b)" role="img" aria-label="Woman with a red scarf"></div>
  <div class="tile" style="left:297px;top:614px;width:144px;background:linear-gradient(180deg,#b7d3ea,#8b7350 40%,#3fc3c6)" role="img" aria-label="Overwater hut in a lagoon"></div>
  <div class="tile" style="left:451px;top:614px;width:298px;background:linear-gradient(120deg,#d8c9a8,#a86a3e 50%,#e8e1d6)" role="img" aria-label="Hotel bedroom with a wooden bed"></div>
  <div class="tile" style="left:759px;top:614px;width:298px;background:linear-gradient(120deg,#e7e3dc,#d9c3ab 50%,#c7c2bd)" role="img" aria-label="Family smiling together at home">
    <div class="tile-caption">
      <div class="play-box"><svg width="26" height="26" viewBox="0 0 26 26"><circle cx="13" cy="13" r="11" fill="none" stroke="#fff" stroke-width="2"/><path d="M10 8l8 5-8 5z" fill="#fff"/></svg></div>
      <span>adversarium ea duo congue</span>
    </div>
  </div>

  <div class="abs social-row">
    <span class="social-dot"></span><span class="social-dot"></span><span class="social-dot"></span><span class="social-dot"></span><span class="social-dot"></span>
  </div>
  <div class="abs view-all">View All
    <svg width="11" height="7" viewBox="0 0 11 7"><path d="M1 1l4.5 4.5L10 1" stroke="var(--accent)" stroke-width="2" fill="none"/></svg></div>
</main>

<footer class="site-footer">
  <div class="abs footer-col" style="left:142px;top:37px"><h4>BUY / BROWSER</h4>
    <ul><li>Roommates</li><li>Cars</li><li>Boats</li><li>Electronics</li><li>Real Estate</li><li>Others</li></ul></div>
  <div class="abs footer-col" style="left:303px;top:38px"><h4>SELL</h4>
    <ul><li>Start Selling</li><li>Login</li><li>Shooting Video</li><li>Uploading Video</li><li>Buying</li></ul></div>
  <div class="abs footer-col" style="left:441px;top:38px"><h4>INFO</h4>
    <ul><li>Vblog</li><li>FAQs</li><li>Terms of Use</li><li>Privacy Policy</li><li>Buyer/Seller Safety</li></ul></div>
  <div class="abs footer-col" style="left:593px;top:38px"><h4>CONTACT</h4>
    <ul><li>Contact Us</li><li>Feedback Form</li><li>Refferal Program</li><li>Business Register</li><li>Subscription</li></ul></div>
  <div class="abs footer-divider"></div>
  <div class="abs newsletter">
    <h4>Stay update with us!</h4>
    <p>Tation patrioque ius id, quidam rationibus sed a pumei adversarium ea duo congue sententiae est cu.</p>
    <div class="subscribe-form"><div class="email">Enter your email address</div><div class="submit">Subscribe</div></div>
  </div>
</footer>

<div class="bottom-bar">
  <div class="abs copyright">© 2013 <b>Pim Sa Ox.</b> All Rights Reserved.</div>
  <div class="abs legal-links"><span>about us</span><span>customer service</span><span>privacy policy</span><span>search terms</span><span>advance search</span><span>contact us</span></div>
</div>

</body>
</html>
```